Fashion Label Startup Business Card Design

Marianne Velk is a startup fashion designer based on the Gold Coast in QLD Australia. Mariannes label " Sorrina by Velk " is based upon taking old world design techniques and infusing them modern twist. The card design should incorporate an old world theme using colours like mustard, ocha, black, white and elements of lace pattern.

Card Details:

Marianne Velk
Fashion Designer
P: 04 0163 5271
E: sorrinabyvelk@mailbrook.net
W: www.threadpage.net/SOrrinaByVelk

```html
<!DOCTYPE html>
<html lang="en">
<head>
<meta charset="utf-8">
<title>Marianne Velk – Business Card</title>
<link rel="stylesheet" href="https://fonts.googleapis.com/css2?family=Pinyon+Script&family=Josefin+Sans:wght@400&display=swap">
<style>
  :root {
    --backdrop: #e6e2de;
    --card-top: #4b3c35;
    --card-bottom: #392b25;
    --ink: #f6f1ec;
    --ink-soft: #e2d9d2;
  }
  * { margin: 0; padding: 0; box-sizing: border-box; }
  html, body {
    width: 1200px;
    height: 1000px;
    overflow: hidden;
    background: var(--backdrop);
  }
  .card {
    position: absolute;
    left: 80px;
    top: 240px;
    width: 1040px;
    height: 520px;
    background: linear-gradient(180deg, var(--card-top) 0%, var(--card-bottom) 100%);
    box-shadow: 0 10px 30px rgba(0, 0, 0, 0.25);
  }
  .card__name {
    position: absolute;
    left: 0;
    right: 0;
    top: 176px;
    text-align: center;
    font-family: "Pinyon Script", cursive;
    font-size: 88px;
    line-height: 1;
    color: var(--ink);
    word-spacing: 18px;
  }
  .card__title {
    position: absolute;
    left: 322px;
    top: 296px;
    font-family: "Josefin Sans", sans-serif;
    font-size: 24px;
    letter-spacing: 0.5px;
    color: var(--ink);
  }
  .card__contacts {
    position: absolute;
    left: 0;
    right: 0;
    top: 444px;
    display: flex;
    justify-content: center;
    align-items: center;
    gap: 20px;
    font-family: "Josefin Sans", sans-serif;
    font-size: 18px;
    letter-spacing: 0.6px;
    color: var(--ink-soft);
  }
  .card__divider {
    width: 8px;
    height: 8px;
    background: var(--ink);
    transform: rotate(45deg);
  }
</style>
</head>
<body>
  <section class="card" aria-label="Business card">
    <h1 class="card__name">Marianne Velk</h1>
    <p class="card__title">Fashion Designer</p>
    <p class="card__contacts">
      <span class="card__phone">04 0163 5271</span>
      <span class="card__divider" aria-hidden="true"></span>
      <span class="card__email">sorrinabyvelk@mailbrook.net</span>
      <span class="card__divider" aria-hidden="true"></span>
      <span class="card__web">www.threadpage.net/SOrrinaByVelk</span>
    </p>
  </section>
</body>
</html>
```